Larkmoor Hospitality Core Values Poster

I would like the layout I put together designed professionally. The poster will be 36" x 24" in landscape format. I would like the font to match the Larkmoor Hospitality font in the middle of the poster. Convert the black and white poster into something colorful so that the icons pop and it is suitable for framing. The website is https://www.larkmoorhospitality.com/ for reference.

```html
<!DOCTYPE html>
<html lang="en">
<head>
<meta charset="utf-8">
<title>Larkmoor Hospitality – Our Core Values</title>
<link rel="stylesheet" href="https://fonts.googleapis.com/css2?family=Cinzel:wght@400;800&family=Nunito:wght@400;800&display=swap">
<style>
  :root {
    --navy: #181b3a;
    --line: #c4e6f7;
    --icon-bg: #7dd3ec;
    --text: #ffffff;
  }
  * { margin: 0; padding: 0; box-sizing: border-box; }
  html, body { width: 1200px; height: 800px; overflow: hidden; background: var(--navy); }
  .poster {
    position: relative;
    width: 1200px;
    height: 800px;
    background: var(--navy);
    color: var(--text);
    font-family: "Nunito", sans-serif;
  }
  .brand {
    position: absolute;
    top: 46px;
    left: 0;
    width: 1200px;
    text-align: center;
    font-family: "Cinzel", serif;
    font-weight: 400;
    color: var(--text);
  }
  .brand-name {
    display: block;
    font-size: 58px;
    line-height: 64px;
    letter-spacing: 0.32em;
    padding-left: 0.32em;
  }
  .brand-sub {
    display: block;
    margin-top: 4px;
    font-size: 24px;
    line-height: 28px;
    letter-spacing: 0.5em;
    padding-left: 0.5em;
  }
  .frame {
    position: absolute;
    inset: 0;
  }
  .values-title {
    position: absolute;
    left: 334px;
    top: 178px;
    width: 530px;
    height: 76px;
    display: flex;
    align-items: center;
    justify-content: center;
    font-family: "Cinzel", serif;
    font-weight: 800;
    font-size: 44px;
    letter-spacing: 0.01em;
  }
  .value-icon {
    position: absolute;
    width: 110px;
    height: 110px;
    border-radius: 50%;
    background: var(--icon-bg);
    transform: translate(-50%, -50%);
  }
  .value-text {
    position: absolute;
    width: 160px;
    transform: translateX(-50%);
    text-align: center;
  }
  .value-name {
    font-weight: 800;
    font-size: 18px;
    line-height: 22px;
    margin-bottom: 4px;
  }
  .value-traits {
    list-style: none;
    font-weight: 400;
    font-size: 15.5px;
    line-height: 22px;
  }
  .value-text.upper { top: 474px; }
  .value-text.lower { top: 607px; }
</style>
</head>
<body>
<main class="poster">
  <header class="brand">
    <span class="brand-name">LARKMOOR</span>
    <span class="brand-sub">HOSPITALITY</span>
  </header>

  <svg class="frame" width="1200" height="800" viewBox="0 0 1200 800" aria-hidden="true">
    <path d="M334 217 H123 A88 88 0 0 0 35 305 V650 A83 83 0 0 0 201 650 V397 A80 80 0 0 1 361 397 V650 A80 80 0 0 0 521 650 V397 A80 80 0 0 1 680 397 V650 A80 80 0 0 0 839 650 V397 A80 80 0 0 1 999 397 V650 A83 83 0 0 0 1165 650 V305 A88 88 0 0 0 1077 217 H864"
          fill="none" stroke="var(--line)" stroke-width="4"/>
    <rect x="334" y="179" width="530" height="75" rx="37.5" fill="none" stroke="var(--line)" stroke-width="4"/>
  </svg>

  <h1 class="values-title">Our Core Values</h1>

  <div class="value-icon" style="left:121px;top:530px" role="img" aria-label="Icon: speech bubble with heart above a group of people"></div>
  <div class="value-icon" style="left:280px;top:397px" role="img" aria-label="Icon: handshake"></div>
  <div class="value-icon" style="left:441px;top:530px" role="img" aria-label="Icon: briefcase and heart balanced on a scale"></div>
  <div class="value-icon" style="left:600px;top:397px" role="img" aria-label="Icon: hotel building with stars"></div>
  <div class="value-icon" style="left:761px;top:530px" role="img" aria-label="Icon: person with rising arrows"></div>
  <div class="value-icon" style="left:919px;top:397px" role="img" aria-label="Icon: crowd of people with a heart"></div>
  <div class="value-icon" style="left:1081px;top:530px" role="img" aria-label="Icon: family inside a house with a heart"></div>

  <section class="value-text lower" style="left:121px">
    <h2 class="value-name">Compassionate</h2>
    <ul class="value-traits"><li>Empathy</li><li>Forgiving</li><li>Listening</li></ul>
  </section>
  <section class="value-text upper" style="left:280px">
    <h2 class="value-name">Respected</h2>
    <ul class="value-traits"><li>Trusted</li><li>Integrity</li><li>Reputation</li></ul>
  </section>
  <section class="value-text lower" style="left:441px">
    <h2 class="value-name">Balance</h2>
    <ul class="value-traits"><li>Health</li><li>Work-Life</li><li>Happiness</li></ul>
  </section>
  <section class="value-text upper" style="left:600px">
    <h2 class="value-name">Accommodating</h2>
    <ul class="value-traits"><li>Guest Driven</li><li>Problem Solving</li><li>Above &amp; Beyond</li></ul>
  </section>
  <section class="value-text lower" style="left:761px">
    <h2 class="value-name">Opportunity</h2>
    <ul class="value-traits"><li>Growth</li><li>Successful</li><li>“Plus”-ing</li></ul>
  </section>
  <section class="value-text upper" style="left:919px">
    <h2 class="value-name">Community</h2>
    <ul class="value-traits"><li>Guest Driven</li><li>Problem Solving</li><li>Above &amp; Beyond</li></ul>
  </section>
  <section class="value-text lower" style="left:1081px">
    <h2 class="value-name">Family</h2>
    <ul class="value-traits"><li>Caring</li><li>Loyalty</li><li>Tradition</li></ul>
  </section>
</main>
</body>
</html>
```